Business Card Design

Contact Information for Business Card

A vertical business card request- a medium & light gray with silverpine tree logo (logo is attached)

Please use Trebuchet font -- if possible- can we use two different color gray? (See pictures attached below)
Info on the front should be the Silverpine tree logo - on the top of the card, followed by the info ...
Card to read: " " indicated what should be on the card --
Name: " Carla Merrow "
Title : "Partner "
" Office: 202.555.0147 "
" Mobile: 202.555.0183 "

Backside of the card - solid medium color gray color w/ address and small message centered in the card - Trebuchet font
to read:

" 718 B North Larkmoor Avenue, NE "
" Washington, DC 20019 "

Then below address to read:
" Fundraising | Event Planning | Political Consulting "

```html
<!DOCTYPE html>
<html lang="en">
<head>
<meta charset="utf-8">
<title>Silverpine Strategies — Business Card</title>
<link rel="stylesheet" href="https://fonts.googleapis.com/css2?family=Open+Sans:wght@400;600;700&display=swap">
<style>
  :root {
    --backdrop: #f1f1f1;
    --card-light: #b1b1b2;
    --card-dark: #67686a;
    --ink-pale: #ececec;
    --ink-soft: #c9c9ca;
    --ink-muted: #bdbdbe;
    --rule: #a9a9aa;
  }
  * { margin: 0; padding: 0; box-sizing: border-box; }
  html, body {
    width: 1200px; height: 782px; overflow: hidden;
    background: var(--backdrop);
    font-family: "Open Sans", "Trebuchet MS", sans-serif;
  }
  .canvas { position: relative; width: 1200px; height: 782px; }

  /* Back of card */
  .card-back {
    position: absolute; left: 135px; top: 340px;
    width: 553px; height: 310px;
    background: var(--card-light);
  }
  .back-brand {
    position: absolute; left: 40px; top: 140px;
    font-size: 20px; font-weight: 400; letter-spacing: 1px;
    color: var(--ink-pale);
  }
  .back-details {
    position: absolute; left: 457px; top: 18px;
    height: 254px;
    writing-mode: vertical-rl;
    transform: rotate(180deg);
    text-align: end;
    font-size: 13px; line-height: 18px; letter-spacing: 0.3px;
    color: var(--ink-pale);
  }
  .back-services { text-transform: uppercase; margin-inline-start: 0; }
  .back-address { margin-left: 12px; }

  /* Front of card */
  .card-front {
    position: absolute; left: 710px; top: 84px;
    width: 326px; height: 568px;
    background: var(--card-dark);
  }
  .brand-name {
    position: absolute; right: 16px; top: 146px;
    text-align: right;
    font-size: 22px; line-height: 24px; font-weight: 400;
    letter-spacing: 0.5px; text-transform: uppercase;
    color: var(--ink-soft);
  }
  .brand-name .brand-sub { display: block; font-size: 12px; line-height: 16px; }
  .person-name {
    position: absolute; left: 17px; top: 443px;
    font-size: 20px; font-weight: 600; letter-spacing: 0.3px;
    text-transform: uppercase; color: var(--ink-pale);
  }
  .person-title {
    position: absolute; left: 0; right: 0; top: 470px;
    display: flex; align-items: center; gap: 4px;
    padding-left: 17px;
    font-size: 11px; letter-spacing: 0.5px; text-transform: uppercase;
    color: var(--ink-muted);
  }
  .person-title::after {
    content: ""; flex: 1; height: 1px; background: var(--rule);
  }
  .contact-list {
    position: absolute; left: 17px; top: 500px;
    list-style: none;
    font-size: 13px; line-height: 17px; letter-spacing: 0.3px;
    color: var(--ink-pale);
  }
  .contact-list li { display: flex; align-items: center; gap: 6px; }
  .contact-list svg { width: 10px; height: 10px; fill: none; stroke: var(--ink-pale); stroke-width: 1.4; }
</style>
</head>
<body>
<main class="canvas">

  <section class="card-back" aria-label="Back of card">
    <p class="back-brand">SILVERPINE</p>
    <div class="back-details">
      <p class="back-services">" Fundraising | Event Planning<br>Political Consulting "</p>
      <p class="back-address">718 B North Larkmoor<br>Avenue, NE Washington, DC 20019</p>
    </div>
  </section>

  <section class="card-front" aria-label="Front of card">
    <p class="brand-name">Silverpine<span class="brand-sub">Strategies</span></p>

    <h1 class="person-name">Carla Merrow</h1>
    <p class="person-title">Partner</p>

    <ul class="contact-list">
      <li>
        <svg viewBox="0 0 10 10" aria-hidden="true"><rect x="2.5" y="0.8" width="5" height="8.4" rx="1"/><line x1="4.3" y1="7.6" x2="5.7" y2="7.6"/></svg>
        <span>202.555.0147</span>
      </li>
      <li>
        <svg viewBox="0 0 10 10" aria-hidden="true"><path d="M2 1.2 L3.6 1 L4.4 3.2 L3.3 4 Q4.3 6 6 6.8 L6.8 5.7 L9 6.4 L8.8 8.1 Q5 8.6 2.6 6.2 Q0.8 4 2 1.2 Z" fill="var(--ink-pale)" stroke="none"/></svg>
        <span>202.555.0183</span>
      </li>
      <li>
        <svg viewBox="0 0 10 10" aria-hidden="true"><rect x="0.8" y="2" width="8.4" height="6"/><polyline points="0.8,2 5,5.4 9.2,2"/></svg>
        <span>carla@silverpinellc.com</span>
      </li>
    </ul>
  </section>

</main>
</body>
</html>
```